EOFYS BANNER REQUIRED FOR HIGH-END BABY PRODUCT

We seel baby beanbags, and we need a banner for our annual END OF FINANCIAL YEAR SALE (EOFYS) about 700x900px.

The promo will be:

THE EOFYS SALE IS ON NOW!
30% OFF ALL ORDERS OVER $149 WITH CODE: EOFYS

We will use this banner for an email marketing campaign, and we will actually need to resize this banner to suit some affiliate marketing sizes too (ie: leaderboard etc), so if you are able to show your design in a few different sizes, that would be great.

We don't have alot of images for you to work off, so it will be your creative design skills that make it great.

Please keep in mind this is for a massive event that we will be competing with alot of other businesses for, as it is an annual event where the whole country goes on sale. We are in the process of building a photo studio so we have attached the images we have to work with now.

I have uploaded some of our patterns for you. This is CONFIDENTIAL. You are welcome to use these patterns in the dsign if you like.

Please, do your best.

Urban mums who crave design and function more than a cheap product.

Baby

• montserrat; intro rust; Pirou

b768aa
e667a6
f68e4e
fece3e
fbf289
add136
cadf82
33b8a4
33a6d7

• One, or both, of the two images upload. They are: IMG.5251 / IMG. 5253
• Would love a toddler in the pic also, if possible...they don't have to be using our beanbag, but there should be a pic of our beanbag there, as if it is waiting for them to use.
• Other brands. Childish themes. Too much vector overload...but some is awesome.

```html
<!DOCTYPE html>
<html lang="en">
<head>
<meta charset="utf-8">
<title>Pipkin – EOFYS Sale</title>
<link rel="stylesheet" href="https://fonts.googleapis.com/css2?family=Fredoka:wght@500;600;700&family=Montserrat:wght@500;700&display=swap">
<style>
  :root {
    --purple: #b768aa;
    --pink: #e667a6;
    --orange: #f68e4e;
    --lime: #add136;
    --soft-green: #cadf82;
    --teal: #33b8a4;
    --blue: #33a6d7;
    --brown: #6f6357;
    --tan: #f2bf83;
    --sky: #a9d2ea;
    --blush: #e0a9cf;
    --citron: #e9ef6c;
    --butter: #fdfbd3;
    --cream: #f3eedc;
    --paper: #ffffff;
  }
  * { margin: 0; padding: 0; box-sizing: border-box; }
  html, body { width: 933px; height: 1200px; overflow: hidden; background: var(--paper); }
  .banner { position: relative; width: 933px; height: 1200px; overflow: hidden; background: var(--paper); font-family: "Fredoka", sans-serif; }
  .layer { position: absolute; inset: 0; }

  .brand { position: absolute; left: 33px; top: 40px; }
  .brand-name { font-family: "Montserrat", sans-serif; font-weight: 500; font-size: 50px; color: var(--brown); letter-spacing: -1px; line-height: 1; }
  .brand-tagline { font-family: "Montserrat", sans-serif; font-weight: 700; font-size: 13px; color: var(--brown); margin-top: 4px; }

  .headline { position: absolute; font-weight: 700; line-height: 1; text-transform: uppercase; white-space: nowrap; }
  .headline-the { left: 232px; top: 176px; font-size: 46px; color: var(--orange); }
  .headline-sale { left: 138px; top: 220px; font-size: 62px; color: var(--purple); }
  .headline-is-on { left: 296px; top: 284px; font-size: 38px; color: var(--lime); }
  .headline-now { left: 420px; top: 266px; font-size: 84px; color: var(--lime); }

  .discount-number { position: absolute; left: 258px; top: 290px; font-weight: 700; font-size: 300px; line-height: 1; color: var(--purple); letter-spacing: -4px; }
  .discount-percent { position: absolute; left: 612px; top: 318px; font-weight: 700; font-size: 125px; line-height: 1; color: var(--purple); transform: scaleX(1.45); transform-origin: left top; }
  .discount-off { position: absolute; left: 610px; top: 460px; font-weight: 700; font-size: 124px; line-height: 1; color: var(--pink); letter-spacing: -4px; }

  .offer-terms { position: absolute; left: 290px; top: 578px; font-weight: 600; font-size: 36px; color: var(--brown); text-transform: uppercase; white-space: nowrap; }

  .promo-code { position: absolute; left: 530px; top: 664px; font-weight: 700; font-size: 42px; text-transform: uppercase; white-space: nowrap; }
  .promo-code .label { color: var(--orange); }
  .promo-code .code { color: var(--brown); }

  .product-photo { position: absolute; left: 40px; top: 680px; width: 484px; height: 390px; border-radius: 46% 46% 30% 30% / 40% 40% 30% 30%; background: linear-gradient(180deg, var(--cream) 0%, #efe6cf 55%, #e6d9bb 100%); }
</style>
</head>
<body>
<main class="banner">

  <svg class="layer color-bands" width="933" height="1200" viewBox="0 0 933 1200" aria-hidden="true">
    <defs>
      <clipPath id="band-edge">
        <path d="M0 1092 Q 300 1040 520 1010 Q 760 985 933 985 L933 1200 L0 1200 Z"/>
      </clipPath>
    </defs>
    <g clip-path="url(#band-edge)">
      <rect x="0" y="900" width="253" height="300" fill="var(--sky)"/>
      <rect x="253" y="1098" width="28" height="102" fill="var(--soft-green)"/>
      <rect x="281" y="1098" width="58" height="102" fill="var(--tan)"/>
      <rect x="339" y="1098" width="54" height="102" fill="var(--brown)"/>
      <rect x="393" y="900" width="127" height="300" fill="var(--citron)"/>
      <rect x="520" y="900" width="105" height="300" fill="var(--butter)"/>
      <rect x="625" y="900" width="113" height="300" fill="var(--blush)"/>
      <rect x="738" y="900" width="48" height="300" fill="var(--tan)"/>
      <rect x="786" y="900" width="107" height="300" fill="var(--brown)"/>
      <rect x="893" y="900" width="40" height="300" fill="var(--soft-green)"/>
    </g>
  </svg>

  <header class="brand">
    <div class="brand-name">Pipkin</div>
    <div class="brand-tagline">comfort, made with care.</div>
  </header>

  <h1 class="headline headline-the">The</h1>
  <div class="headline headline-sale">EOFYS Sale</div>
  <div class="headline headline-is-on">Is On</div>
  <div class="headline headline-now">Now!</div>

  <svg class="layer burst" width="933" height="1200" viewBox="0 0 933 1200" aria-hidden="true">
    <g stroke="var(--blue)" stroke-width="7" stroke-linecap="round">
      <line x1="160" y1="355" x2="210" y2="368"/>
      <line x1="168" y1="425" x2="218" y2="422"/>
      <line x1="170" y1="490" x2="218" y2="474"/>
      <line x1="185" y1="545" x2="222" y2="522"/>
    </g>
    <g stroke="var(--teal)" stroke-width="7" stroke-linecap="round">
      <line x1="812" y1="318" x2="775" y2="345"/>
      <line x1="840" y1="380" x2="792" y2="392"/>
      <line x1="848" y1="432" x2="800" y2="432"/>
      <line x1="850" y1="490" x2="805" y2="472"/>
    </g>
  </svg>

  <div class="discount-number">30</div>
  <div class="discount-percent">%</div>
  <div class="discount-off">OFF</div>

  <p class="offer-terms">All orders over $149 with</p>

  <svg class="layer code-ribbon" width="933" height="1200" viewBox="0 0 933 1200" aria-hidden="true">
    <path d="M462 648 L845 656 L820 690 L852 722 L478 728 L500 690 Z" fill="none" stroke="var(--soft-green)" stroke-width="5" stroke-linejoin="round"/>
    <path d="M478 660 L830 664 L812 690 L834 714 L492 718 L510 690 Z" fill="none" stroke="var(--soft-green)" stroke-width="3" stroke-linejoin="round"/>
  </svg>
  <div class="promo-code"><span class="label">Code:</span> <span class="code">EOFYS</span></div>

  <div class="product-photo" role="img" aria-label="Photo of a baby resting in a cream and bird-print beanbag on a wooden rocking base"></div>

</main>
</body>
</html>
```